写真挿入は無し、メニュー、営業時間も別看板がありますので記載不要です。添付のロゴとイラストを挿入してください。看板は両面ですが1デザインでも構いません。
⚪店名 雪見坂ことり亭
⚪定食 お酒 または、お食事 呑み処 など(デザインとのバランスでお願いします。)
⚪お気軽にどうぞ、気軽に来店ください など(安心して気軽に入店しやすくなる1フレーズ)
⚪イラストにふき出しで発声させてください。(フレーズはお任せします。)
⚪サイズは450mm×1300mmで縦長です。納品はaiデータです。
⚪文字色、全体的なデザインはお任せですが、背景色は薄ピンクが希望色です。グラデーションも好きです。イラスト、ロゴとのバランスでお願いします。
私ai使えませんので確認は別形式でお願いします。

見やすくバランスが良く丁度良いです。

また、よろしくお願いいたします。

```html
<!DOCTYPE html>
<html lang="ja">
<head>
<meta charset="utf-8">
<title>雪見坂ことり亭 のぼり旗</title>
<link href="https://fonts.googleapis.com/css2?family=Yuji+Mai&family=Zen+Old+Mincho:wght@400;700&display=swap" rel="stylesheet">
<style>
  :root{
    --sheet:#ffffff;
    --pink-top:#f0aec2;
    --pink-mid:#f8d5df;
    --pink-low:#fdf0f3;
    --brand-brown:#7a4320;
    --accent-red:#c8343c;
    --speech-line:#b05070;
    --caption:#555555;
    --edge:#d8c4ca;
  }
  *{margin:0;padding:0;box-sizing:border-box}
  html,body{width:667px;height:1200px;overflow:hidden;background:var(--sheet)}
  .sheet{position:relative;width:667px;height:1200px}
  .banner{
    position:absolute;left:190px;top:55px;width:287px;height:1035px;
    background:linear-gradient(180deg,var(--pink-top) 0%,var(--pink-mid) 35%,var(--pink-low) 70%,#ffffff 100%);
    border:1px solid var(--edge);overflow:hidden;
  }
  .blossom-field{position:absolute;inset:0;
    background:radial-gradient(circle at 80% 20%,rgba(255,255,255,.55),transparent 40%),
               radial-gradient(circle at 20% 60%,rgba(255,255,255,.45),transparent 35%);}
  .genre{
    position:absolute;left:28px;top:95px;display:flex;flex-direction:row-reverse;gap:6px;
    font-family:"Zen Old Mincho",serif;color:var(--accent-red);font-size:16px;
    writing-mode:vertical-rl;
  }
  .genre span{display:block}
  .genre .rule{width:1px;background:var(--accent-red);writing-mode:horizontal-tb}
  .shop-name{font-family:"Yuji Mai",serif;color:var(--brand-brown);position:absolute;
    writing-mode:vertical-rl;font-size:96px;line-height:1;letter-spacing:-4px}
  .shop-name.upper{left:150px;top:30px}
  .shop-name.lower{left:30px;top:215px}
  .romaji{position:absolute;left:140px;top:410px;font-family:"Zen Old Mincho",serif;
    color:var(--brand-brown);font-size:15px;line-height:1.2;text-align:center;width:140px}
  .seal{position:absolute;left:18px;top:600px;font-family:"Zen Old Mincho",serif;
    color:var(--accent-red);font-size:11px;writing-mode:vertical-rl;display:flex;align-items:center;gap:3px}
  .seal i{display:block;width:9px;height:9px;border:1.5px solid var(--accent-red);border-radius:50%}
  .mascot{position:absolute;left:118px;top:510px;width:140px;height:475px;border-radius:60px 60px 20px 20px;
    background:linear-gradient(180deg,#f4a6c0 0%,#f4a6c0 22%,#8fb07a 40%,#e98bb0 70%,#c7e0b8 100%);opacity:.85}
  .speech{position:absolute;left:25px;top:725px;width:110px;height:240px}
  .speech-text{position:absolute;left:40px;top:750px;writing-mode:vertical-rl;
    font-family:"Zen Old Mincho",serif;font-size:17px;line-height:1.5;color:#333}
  .size-note{position:absolute;left:0;width:667px;top:1130px;text-align:left;padding-left:222px;
    font-family:"Zen Old Mincho",serif;font-size:14px;color:var(--caption)}
</style>
</head>
<body>
<div class="sheet">
  <div class="banner">
    <div class="blossom-field" role="img" aria-label="淡い桜の花びら模様"></div>
    <div class="genre"><span>お食事</span><span class="rule"></span><span>呑み処</span></div>
    <div class="shop-name upper">雪見坂</div>
    <div class="shop-name lower">ことり亭</div>
    <p class="romaji">yukimizaka<br>kotoritei</p>
    <div class="seal"><i></i>ことり亭</div>
    <div class="mascot" role="img" aria-label="桜色の髪で着物と袴姿の看板娘イラスト"></div>
    <svg class="speech" viewBox="0 0 110 240" aria-hidden="true">
      <path d="M55 4 C95 4 100 40 100 120 C100 200 95 236 55 236 C15 236 10 200 10 120 C10 40 15 4 55 4 Z" fill="#ffffff" stroke="var(--speech-line)" stroke-width="1.5"/>
      <path d="M98 70 L112 58 L100 88" fill="#ffffff" stroke="var(--speech-line)" stroke-width="1.5"/>
    </svg>
    <p class="speech-text">お気軽に<br>ご来店ください。</p>
  </div>
  <p class="size-note">サイズ :450mm×1300mm</p>
</div>
</body>
</html>
```